LITTLE DESIGN WORK REQUIRED!

UPDATE: WE WEREN'T OVERLY ECSTATIC WITH THE DESIGNS WE WERE RECEIVING SO WE DID MOST OF THE DESIGN WORK OURSELVES...

PLEASE SEE THE NEWLY ATTACHED PPT DOC TO VIEW NEARLY EXACT REPLICAS OF WHAT WE WANT THE SITE TO LOOK LIKE. WE NOW NEED YOUR HELP TO MAKE IT LOOK LIKE SOMETHING WORTHY OF THE WEB.

NO CODING REQUIRED - EXPECTED OUTPUT PSD FILES

Hi everyone!

We're looking for a designer to work their magic for our site! We're a not-for-profit program aimed at helping young people realise their potential!

In the attached PPT file, you'll notice we've already DESIGNED THE ENTIRE SITE IN POWERPOINT. Now, we need YOU to make the small changes we requested in the document as well as design the whole thing in psd.

Any questions, don't hesitate to ask.

Brook-Rise
Updates

We've done about 95% of the design for you. Please fine-tune it. See the newly attached PPT doc for details. 

The best two designs will win. This project closes on Friday - please message us if you are absolutely sure you cannot make the deadline.

Thanks,
Brook-Rise

```html
<!DOCTYPE html>
<html lang="en">
<head>
<meta charset="utf-8">
<title>Brook-Rise</title>
<link href="https://fonts.googleapis.com/css2?family=Open+Sans:ital,wght@0,400;0,600;0,700;0,800;1,400;1,700&family=Arimo:wght@400;700&display=swap" rel="stylesheet">
<style>
:root{
  --green:#6cb800;--green-light:#9be000;--green-dark:#4f9a00;
  --blue:#2f58a8;--blue-title:#1f4f9c;--orange:#e07a00;--red:#c70000;
  --ink:#333;--muted:#666;--faint:#999;--line:#d6d6d6;
  --paper:#fff;--panel:#f7f7f7;--grey-btn:#6d6d6d;
  --footer:#5f5f5f;--sand:#c9ad7a;--sand-light:#efe4cc;--social:#4a64a0;
}
*{box-sizing:border-box;margin:0;padding:0}
html,body{width:1200px;height:2175px;overflow:hidden}
body{position:relative;font-family:"Arimo",Arial,sans-serif;color:var(--ink);
  background:radial-gradient(ellipse at 50% 50%,var(--sand-light) 0%,#e2cfa6 55%,var(--sand) 100%);}
.abs{position:absolute}
.header{left:0;top:0;width:1200px;height:145px;background:linear-gradient(#fff,#ececec);box-shadow:0 2px 6px rgba(0,0,0,.25);z-index:2}
.brand{left:138px;top:50px;display:flex;align-items:center;gap:10px;font-family:"Open Sans",sans-serif;font-weight:800;font-size:38px;color:#222;letter-spacing:-1px}
.brand-mark{width:30px;height:30px;background:var(--green)}
.quote{right:120px;top:38px;text-align:right;font-family:"Open Sans",sans-serif;font-style:italic;font-size:22px;line-height:30px;color:#666}
.quote::before{content:"\201C";position:absolute;left:-38px;top:-10px;font-size:60px;color:#ccc;font-style:normal}
.quote::after{content:"\201D";position:absolute;right:-38px;top:20px;font-size:60px;color:#ccc;font-style:normal}
.quote-by{right:130px;top:112px;display:flex;align-items:center;gap:10px;font-size:14px;color:#555}
.share{background:var(--social);color:#fff;font-size:12px;font-weight:700;padding:2px 8px;border-radius:2px;display:flex;gap:5px;align-items:center}
.share i{width:9px;height:9px;background:#fff;display:block}
.column{left:120px;top:145px;width:960px;height:1847px;background:var(--paper)}
.nav{left:130px;top:168px;display:flex;gap:20px}
.nav a{width:140px;height:50px;display:flex;align-items:center;justify-content:center;border-radius:6px;font-family:"Open Sans",sans-serif;font-size:17px;color:#fff;text-decoration:none;background:linear-gradient(#9a9a9a,#5a5a5a);box-shadow:0 2px 3px rgba(0,0,0,.3)}
.nav a.active{background:linear-gradient(var(--green-light),var(--green));color:#234}
.hero{left:130px;top:236px;width:620px;height:346px;border-radius:8px;background:linear-gradient(#f6e6cc 0%,#e9cf9e 55%,#b59560 100%)}
.feats{left:770px;top:236px;width:300px;height:346px;border-radius:8px;background:linear-gradient(var(--green-light),var(--green-dark));color:#fff;text-align:center;font-family:"Open Sans",sans-serif}
.feats h2{margin-top:52px;font-size:52px;font-weight:800;letter-spacing:2px;text-shadow:0 2px 3px rgba(0,0,0,.3)}
.feats p{margin-top:10px;font-size:30px;font-weight:700;line-height:40px}
.dots{left:132px;top:594px;display:flex;gap:6px}
.dots i{width:16px;height:16px;border-radius:50%;background:var(--green);display:block}
.dots i:nth-child(2){background:#9a8fc4}
h2.section{font-family:"Open Sans",sans-serif;font-weight:400;font-size:30px;color:#222}
.welcome-text{left:130px;top:680px;width:560px;font-size:14px;line-height:21px}
.more{font-size:13px;font-weight:700;color:var(--green-dark);display:flex;gap:8px;align-items:center}
.more::before{content:"\2192";color:#222;font-size:18px;font-weight:400}
.like-row{left:772px;top:638px;width:300px;display:flex;gap:6px;font-size:12px;line-height:20px;color:#555}
.like-btn{border:1px solid #bbb;background:#eee;font-size:11px;padding:0 5px;height:18px;line-height:16px;color:#444}
.sq{width:16px;height:16px;background:var(--social);display:block;flex:none}
.activity{left:770px;top:700px;width:300px;height:312px;border:1px solid var(--social);background:#fff;font-size:12.5px}
.activity h3{background:var(--social);color:#fff;font-size:13px;padding:7px 14px}
.act{display:flex;gap:8px;padding:10px 14px 0 12px}
.act b{font-weight:400;color:#333;display:block;line-height:16px}
.act small{font-size:10px;color:#888}
.activity .foot{position:absolute;bottom:0;left:0;right:0;border-top:1px solid #ddd;padding:4px 12px;font-size:10px;color:#666;display:flex;gap:6px}
.cat{left:130px;width:540px;height:270px;border:2px solid;background:#fff}
.cat-head{height:34px;color:#fff;font-family:"Open Sans",sans-serif;font-style:italic;font-weight:700;font-size:18px;display:flex;justify-content:space-between;padding:0 14px;align-items:center}
.cat.discover{border-color:var(--blue)} .discover .cat-head{background:linear-gradient(#4d75c6,var(--blue))}
.cat.design{border-color:var(--orange)} .design .cat-head{background:linear-gradient(#f09a25,var(--orange))}
.cat.build{border-color:var(--red)} .build .cat-head{background:linear-gradient(#e02020,var(--red))}
.cat.achieve{border-color:var(--green)} .achieve .cat-head{background:linear-gradient(var(--green-light),var(--green))}
.posts{display:flex;gap:78px;padding:20px 0 0 43px}
.post{width:187px}
.thumb{height:120px}
.post h4{margin-top:14px;font-size:17px;color:var(--blue-title);font-weight:700}
.post p{font-size:12px;line-height:18px;color:#444;text-align:justify}
.popular{left:770px;top:1110px;width:300px;height:430px;border:1px solid #ddd;background:var(--panel)}
.pop{height:85px;position:relative;padding:18px 14px 0 58px;font-size:12px;line-height:18px;color:#444}
.pop span{position:absolute;left:10px;top:14px;font-family:"Open Sans",sans-serif;font-weight:800;font-size:44px;color:#e4e4e4}
.pop small{display:block;font-size:10px;color:#888;margin-top:4px}
.people{left:770px;top:1620px;width:300px;height:372px;border:1px solid #ddd;background:var(--panel)}
.person{position:absolute;left:14px;width:275px}
.person .photo{position:absolute;left:0;top:0;width:114px;height:130px}
.person .info{margin-left:126px;font-size:12px;line-height:17px;color:#999}
.person h4{color:var(--blue-title);font-size:15px;margin-bottom:3px}
.person .role{text-align:right;color:#333;margin-top:14px}
.person .more{justify-content:flex-end;margin-top:8px}
.footer{left:0;top:1992px;width:1200px;height:148px;background:var(--footer);color:#eee}
.footer h5{font-size:14px;font-weight:700;margin-bottom:6px}
.footer p{font-size:11px;line-height:14px;color:#ddd}
.search-input{width:298px;height:32px;border-radius:6px;background:linear-gradient(#fff,#ddd)}
.search-btn{position:absolute;right:0;top:54px;background:#111;color:#fff;font-size:12px;font-weight:700;padding:3px 8px;border-radius:3px}
.copy{left:0;top:2140px;width:1200px;height:35px;background:var(--green);color:#fff;font-size:12px;padding:9px 132px}
</style>
</head>
<body>
<header class="header abs">
  <div class="brand abs"><i class="brand-mark"></i>Brook-Rise</div>
  <blockquote class="quote abs">What would you do if you<br>knew you could not fail?</blockquote>
  <div class="quote-by abs">R. Halloway <span class="share"><i></i>Share</span></div>
</header>

<main class="column abs"></main>

<nav class="nav abs">
  <a class="active">HOME</a><a>ABOUT US</a><a>RESOURCES</a><a>WORKSHOPS</a><a>AMBASSADORS</a><a>FEATS</a>
</nav>

<div class="hero abs" role="img" aria-label="Three elephants walking through golden savanna grass"></div>
<section class="feats abs"><h2>FEATS</h2><p>Challenges that<br>dare you to<br>push yourself.</p></section>
<div class="dots abs"><i></i><i></i><i></i><i></i></div>

<h2 class="section abs" style="left:130px;top:630px">Welcome to Brook Rise</h2>
<p class="welcome-text abs">Brook-Rise is a not-for-profit program aimed at helping people – especially young people – set and achieve authentic, meaningful, and audacious goals.</p>
<a class="more abs" style="left:130px;top:734px">Read More</a>

<div class="like-row abs"><span class="like-btn">Like</span><i class="sq"></i><span>22 People like this, Be the first of your friends.</span></div>
<aside class="activity abs">
  <h3>Recent Activity</h3>
  <div class="act"><i class="sq"></i><div><b>Calling All Entrepreneurs- Come Hack with us!</b><small>1,891 people shared this.</small></div></div>
  <div class="act"><i class="sq"></i><div><b>Platform Updates: Improved Dev Site, Documentation, and more</b><small>1,866 people shared this.</small></div></div>
  <div class="act"><i class="sq"></i><div><b>Application Roles and Security Features</b><small>1,260 people shared this.</small></div></div>
  <div class="act"><i class="sq"></i><div><b>The Next Step for Circle Credits</b><small>3,383 people shared this.</small></div></div>
  <div class="act"><i class="sq"></i><div><b>HTML5 Games 0.1</b><small>752 people shared this.</small></div></div>
  <div class="foot"><i class="sq" style="width:12px;height:12px"></i>Circlebook social plugin</div>
</aside>

<h2 class="section abs" style="left:130px;top:772px">Recent Post</h2>

<section class="cat discover abs" style="top:824px">
  <div class="cat-head"><span>Discover</span><span>?</span></div>
  <div class="posts">
    <article class="post"><div class="thumb" role="img" aria-label="Students studying together on the grass" style="background:linear-gradient(#7aa04a,#4c6e2c)"></div><h4>Title A</h4><p>Lorem ipsum dolor amet conse ctetur adipisicing elit...</p></article>
    <article class="post"><div class="thumb" role="img" aria-label="Silhouette of a person raising arms against blue sky" style="background:linear-gradient(#1d4fb0,#6aa0e6 60%,#1a2a40)"></div><h4>Title B</h4><p>Lorem ipsum dolor amet conse ctetur adipisicing elit...</p></article>
  </div>
</section>
<section class="cat design abs" style="top:1110px">
  <div class="cat-head"><span>Design</span><span>?</span></div>
  <div class="posts">
    <article class="post"><div class="thumb" role="img" aria-label="Hands turning pages of a report" style="background:linear-gradient(#3a3a3a,#d8d8d8)"></div><h4>Title C</h4><p>Lorem ipsum dolor amet conse ctetur adipisicing elit...</p></article>
    <article class="post"><div class="thumb" role="img" aria-label="Sprinter running on a track" style="background:linear-gradient(90deg,#9bbf3a,#d8c860,#c05a30)"></div><h4>Title D</h4><p>Lorem ipsum dolor amet conse ctetur adipisicing elit...</p></article>
  </div>
</section>
<section class="cat build abs" style="top:1398px">
  <div class="cat-head"><span>Build</span><span>?</span></div>
  <div class="posts">
    <article class="post"><div class="thumb" role="img" aria-label="Business team in an office" style="background:linear-gradient(#f2f2f2,#6a6a6a)"></div><h4>Title E</h4><p>Lorem ipsum dolor amet conse ctetur adipisicing elit...</p></article>
    <article class="post"><div class="thumb" role="img" aria-label="Silhouette of a person raising arms against blue sky" style="background:linear-gradient(#1d4fb0,#6aa0e6 60%,#1a2a40)"></div><h4>Title F</h4><p>Lorem ipsum dolor amet conse ctetur adipisicing elit...</p></article>
  </div>
</section>
<section class="cat achieve abs" style="top:1685px">
  <div class="cat-head"><span>Achieve</span><span>?</span></div>
  <div class="posts">
    <article class="post"><div class="thumb" role="img" aria-label="Hands turning pages of a report" style="background:linear-gradient(#3a3a3a,#d8d8d8)"></div><h4>Title G</h4><p>Lorem ipsum dolor amet conse ctetur adipisicing elit...</p></article>
    <article class="post"><div class="thumb" role="img" aria-label="Students studying together on the grass" style="background:linear-gradient(#7aa04a,#4c6e2c)"></div><h4>Title H</h4><p>Lorem ipsum dolor amet conse ctetur adipisicing elit...</p></article>
  </div>
</section>

<h2 class="section abs" style="left:770px;top:1064px">Popular Post</h2>
<aside class="popular abs">
  <div class="pop"><span>1.</span>Lorem ipsum dolor amet conse ctetur adipisicing elit...<small>587 views</small></div>
  <div class="pop"><span>2.</span>Lorem ipsum dolor amet conse ctetur adipisicing elit...<small>587 views</small></div>
  <div class="pop"><span>3.</span>Lorem ipsum dolor amet conse ctetur adipisicing elit...<small>587 views</small></div>
  <div class="pop"><span>4.</span>Lorem ipsum dolor amet conse ctetur adipisicing elit...<small>587 views</small></div>
  <div class="pop"><span>5.</span>Lorem ipsum dolor amet conse ctetur adipisicing elit...<small>587 views</small></div>
</aside>

<h2 class="section abs" style="left:770px;top:1570px">Get to Know Us</h2>
<aside class="people abs">
  <div class="person" style="top:20px">
    <div class="photo" role="img" aria-label="Portrait of a young entrepreneur" style="background:linear-gradient(#c9b7a0,#5a6a7a)"></div>
    <div class="info"><h4>Tom Reid</h4>Lorem ipsum dolor amet conse ctetur adipisicing elit...<p class="role">Young entrepreneur &amp;<br>Brook-Rise Ambassador</p><a class="more">Meet Tom</a></div>
  </div>
  <div class="person" style="top:185px">
    <div class="photo" role="img" aria-label="Tennis player mid-swing on court" style="background:linear-gradient(#d0d8e0,#c66a80)"></div>
    <div class="info"><h4>Ana Cole</h4>Lorem ipsum dolor amet conse ctetur adipisicing elit...<p class="role">Professional athlete &amp;<br>Brook-Rise Ambassador</p><a class="more">Meet Ana</a></div>
  </div>
</aside>

<footer class="footer abs">
  <div class="abs" style="left:130px;top:22px">
    <h5>Contact Us</h5>
    <p>USA<br>42 Wren Lane, Arbor Vale, AV3 7QT.<br>Freephone: &nbsp;+1 800 555 0147<br>Telephone: &nbsp;+1 800 555 0147<br>Fax: &nbsp;&nbsp;&nbsp;&nbsp;&nbsp;&nbsp;&nbsp;&nbsp;&nbsp;&nbsp;&nbsp;+1 800 555 0147<br>Email: &nbsp;mail@brookrise.org</p>
  </div>
  <div class="abs" style="left:484px;top:22px">
    <h5>Page Directory</h5>
    <p>Home<br>About Us<br>Resources<br>Workshops<br>Amdassadors<br>Feats</p>
  </div>
  <div class="abs" style="left:772px;top:22px;width:298px;height:90px">
    <h5>Search Site</h5>
    <div class="search-input"></div>
    <span class="search-btn">&#9906; Search</span>
  </div>
</footer>
<div class="copy abs">© 2012 Brook-Rise &nbsp;All Rights Reserved</div>
</body>
</html>
```